Makeup Artist Requires Business Card design

Hi

I am looking for a business card design to market my makeup artist business. I operate under my own name Mara Veldt and I would like to keep the design of the card very simplistic and chic - something that keeps both my name and profession (makeup artist) the focus of the card. I would like it to be a style that is eyecatching to the reader (i am open to anything unusual) but upmarket.

Target Market(s)

women, magazine/beauty/fashion editors, photographers.

Industry/Entity Type

Business

Requirements
Must have
• Must contain:

Phone number: 0418 372 915
Website: www.maraveldt.com.au
email: contact@maraveldt.com.au

(although you don't need to have prefaced these with the words phone number, website etc :))
Should not have
• I am not looking for anything overly colorful - my preference is to keep the card dark if possible.

```html
<!DOCTYPE html>
<html lang="en">
<head>
<meta charset="utf-8">
<title>Mara Veldt — Business Card</title>
<link href="https://fonts.googleapis.com/css2?family=Allura&family=Poppins:wght@300;400&display=swap" rel="stylesheet">
<style>
  :root {
    --backdrop: #d9d9d9;
    --card: #1b1b1b;
    --card-edge: #131313;
    --card-sheen: #262626;
    --ink: #050505;
    --ink-soft: #0c0c0c;
    --band: #2a2a2a;
  }
  * { margin: 0; padding: 0; box-sizing: border-box; }
  html, body {
    width: 1200px;
    height: 1000px;
    overflow: hidden;
    background: var(--backdrop);
  }
  .canvas {
    position: relative;
    width: 1200px;
    height: 1000px;
  }
  .card {
    position: absolute;
    left: 280px;
    width: 640px;
    height: 366px;
    background: linear-gradient(160deg, var(--card-sheen) 0%, var(--card) 45%, var(--card-edge) 100%);
    box-shadow: 0 14px 30px rgba(0,0,0,0.28);
  }
  .card--front { top: 70px; }
  .card--back  { top: 510px; }

  .front__name {
    position: absolute;
    top: 104px;
    left: 0;
    width: 100%;
    text-align: center;
    font-family: "Allura", cursive;
    font-size: 96px;
    line-height: 1;
    color: var(--ink);
  }
  .front__role {
    position: absolute;
    top: 238px;
    left: 0;
    width: 100%;
    text-align: center;
    font-family: "Poppins", sans-serif;
    font-weight: 300;
    font-size: 13px;
    letter-spacing: 4px;
    color: var(--ink-soft);
  }

  .back__band {
    position: absolute;
    left: 150px;
    top: 100px;
    width: 340px;
    height: 166px;
    background: linear-gradient(180deg, transparent 0%, var(--band) 30%, var(--band) 70%, transparent 100%);
  }
  .contact {
    position: absolute;
    left: 170px;
    top: 128px;
    list-style: none;
    font-family: "Poppins", sans-serif;
    font-weight: 400;
    font-size: 17px;
    letter-spacing: 3px;
    color: var(--ink);
  }
  .contact__item {
    display: flex;
    align-items: center;
    gap: 12px;
    height: 36px;
  }
  .contact__icon {
    width: 14px;
    height: 14px;
    flex: none;
  }
</style>
</head>
<body>
<main class="canvas">
  <section class="card card--front" aria-label="Card front">
    <h1 class="front__name">Mara Veldt</h1>
    <p class="front__role">makeup artist</p>
  </section>

  <section class="card card--back" aria-label="Card back">
    <div class="back__band"></div>
    <ul class="contact">
      <li class="contact__item">
        <svg class="contact__icon" viewBox="0 0 14 14" aria-hidden="true">
          <path d="M3 1 L5.5 1 L6.5 4 L5 5.2 C5.8 7 7 8.2 8.8 9 L10 7.5 L13 8.5 L13 11 C13 12 12 13 11 13 C5.5 12.5 1.5 8.5 1 3 C1 2 2 1 3 1 Z" fill="#050505"/>
        </svg>
        <span>0418 372 915</span>
      </li>
      <li class="contact__item">
        <svg class="contact__icon" viewBox="0 0 14 14" aria-hidden="true">
          <circle cx="7" cy="7" r="5.8" fill="none" stroke="#050505" stroke-width="1.4"/>
          <path d="M1.2 7 H12.8 M7 1.2 C4.5 4 4.5 10 7 12.8 M7 1.2 C9.5 4 9.5 10 7 12.8" fill="none" stroke="#050505" stroke-width="1.1"/>
        </svg>
        <span>www.maraveldt.com.au</span>
      </li>
      <li class="contact__item">
        <svg class="contact__icon" viewBox="0 0 14 14" aria-hidden="true">
          <rect x="1" y="3" width="12" height="8.5" fill="none" stroke="#050505" stroke-width="1.3"/>
          <path d="M1 3 L7 8 L13 3" fill="none" stroke="#050505" stroke-width="1.3"/>
        </svg>
        <span>contact@maraveldt.com.au</span>
      </li>
    </ul>
  </section>
</main>
</body>
</html>
```